Beacon Advisory Website

I currently have a website www.beaconadvisoryinc.example. We are a IT Consulting Company. Our website will pretty much tell out our services. I am looking to enhance my website and make it look more professional. Looking for very classy and Contemporary look and design for my website.

Industry/Entity Type

It Company

```html
<!DOCTYPE html>
<html lang="en">
<head>
<meta charset="utf-8">
<title>Beacon Advisory – IT Consulting</title>
<link href="https://fonts.googleapis.com/css2?family=Oswald:wght@500;600&family=Roboto:wght@400;500;700&family=Open+Sans:wght@400;600;700&display=swap" rel="stylesheet">
<style>
:root{
  --brand:#0a9fdc;
  --brand-dark:#0b84bd;
  --black:#000;
  --ink:#222;
  --muted:#555;
  --light:#f3f2f2;
  --white:#fff;
  --orange:#f25a1f;
  --sky:#2ba9ea;
  --navy:#1b55a6;
  --green:#5ca72b;
  --charcoal:#1f1f1f;
  --footer:#2c2c2c;
  --footer-deep:#1d1d1d;
  --footer-text:#b9b9b9;
}
*{box-sizing:border-box;margin:0;padding:0}
html,body{width:1200px;height:2476px;overflow:hidden}
body{font-family:"Open Sans",Arial,sans-serif;color:var(--ink);background:var(--white);position:relative}
section,header,footer{position:relative;width:1200px;overflow:hidden}

/* top bar */
.topbar{height:46px;background:var(--brand);color:var(--white);font-size:15px}
.topbar .contact{position:absolute;left:61px;top:0;height:46px;display:flex;align-items:center;gap:20px}
.topbar .contact span{display:flex;align-items:center;gap:10px}
.topbar .ico{width:22px;height:22px;background:var(--navy);border-radius:3px;display:flex;align-items:center;justify-content:center}
.topbar .follow{position:absolute;right:61px;top:0;height:46px;display:flex;align-items:center}
.topbar .follow em{font-style:normal;margin-right:14px}
.topbar .follow i{width:46px;height:46px;border-left:1px solid rgba(255,255,255,.35);display:flex;align-items:center;justify-content:center}
.topbar .follow i:last-child{border-right:1px solid rgba(255,255,255,.35)}
.topbar .follow b{width:26px;height:26px;border-radius:50%;background:var(--brand-dark);border:1px solid rgba(255,255,255,.5)}

/* nav */
.nav{height:91px;background:var(--black)}
.brand{position:absolute;left:61px;top:24px;display:flex;align-items:center;gap:12px}
.brand .mark{width:40px;height:40px;background:var(--brand)}
.brand .name{font-family:"Roboto",sans-serif;font-weight:700;font-size:24px;color:var(--brand)}
.menu{position:absolute;right:61px;top:0;height:91px;display:flex;gap:44px;list-style:none;font-family:"Roboto",sans-serif;font-size:14px}
.menu li{color:#8d8d8d;display:flex;align-items:center;position:relative}
.menu li.active{color:var(--brand)}
.menu li.active::after{content:"";position:absolute;left:0;right:0;bottom:0;height:3px;background:var(--brand)}

/* hero */
.hero{height:553px;background:linear-gradient(120deg,#3d4752 0%,#2a323b 40%,#1c232b 100%);text-align:center;color:var(--white)}
.hero .photo{position:absolute;inset:0;background:radial-gradient(ellipse at 30% 70%,rgba(120,130,140,.35),transparent 60%),radial-gradient(ellipse at 80% 20%,rgba(90,110,90,.3),transparent 50%)}
.hero h1{position:absolute;top:120px;left:0;width:100%;font-family:"Oswald",sans-serif;font-weight:600;font-size:46px;letter-spacing:.5px}
.hero .line1{position:absolute;top:184px;width:100%;font-size:15px;font-weight:600}
.hero .line2{position:absolute;top:200px;width:100%;font-size:15px;font-weight:600}
.hero .line2 strong{font-family:"Oswald",sans-serif;font-size:46px;font-weight:600;vertical-align:-10px;margin:0 6px}
.btn{display:inline-block;background:var(--brand);color:var(--white);font-family:"Roboto",sans-serif;font-weight:700;text-transform:uppercase}
.hero .btn{position:absolute;left:508px;top:292px;width:183px;height:55px;line-height:55px;font-size:15px}

/* welcome */
.welcome{height:313px;background:var(--white)}
.welcome svg.bg{position:absolute;left:0;top:0}
.welcome h2{position:absolute;left:61px;top:34px;font-family:"Roboto",sans-serif;font-weight:500;font-size:25px;display:flex;align-items:center;gap:14px}
.welcome h2 i{width:26px;height:26px;background:var(--brand);display:inline-block}
.welcome .copy{position:absolute;left:61px;top:80px;width:510px;font-size:12.5px;line-height:20px;color:#333}
.welcome .copy p{margin-bottom:4px}
.welcome .btn{position:absolute;left:61px;top:248px;width:90px;height:31px;line-height:31px;text-align:center;font-size:12px}
.welcome .devices{position:absolute;left:800px;top:60px;width:280px;height:210px;border-radius:14px;background:linear-gradient(160deg,#3b4756,#1d2a3a 60%,#5a8fc4)}

/* services */
.services{height:442px;background:var(--light)}
.section-title{position:absolute;left:0;width:100%;text-align:center;font-family:"Roboto",sans-serif;font-weight:700;font-size:23px;color:var(--ink)}
.services .section-title{top:57px}
.card{position:absolute;top:127px;width:193px;height:267px;box-shadow:0 8px 10px -6px rgba(0,0,0,.25)}
.card .pic{height:129px}
.card .body{height:138px;color:var(--white);text-align:center;padding-top:24px}
.card h3{font-family:"Roboto",sans-serif;font-weight:700;font-size:13px;text-transform:uppercase}
.card p{font-size:11.5px;line-height:18px;margin:10px 12px 0}
.card .more{display:block;font-family:"Roboto",sans-serif;font-weight:700;font-size:11px;margin-top:15px}
.c1{left:61px}.c1 .body{background:var(--orange)}.c1 .pic{background:linear-gradient(135deg,#3a2a6a,#6a4fb0)}
.c2{left:282px}.c2 .body{background:var(--sky)}.c2 .pic{background:linear-gradient(135deg,#c9d9ea,#6f8fb5)}
.c3{left:503px}.c3 .body{background:var(--navy)}.c3 .pic{background:linear-gradient(135deg,#f4f7fa,#bfd6e6)}
.c4{left:724px}.c4 .body{background:var(--green)}.c4 .pic{background:linear-gradient(135deg,#2d3033,#6b6e70)}
.c5{left:945px}.c5 .body{background:var(--charcoal)}.c5 .pic{background:linear-gradient(135deg,#9fb5c5,#3c4d5a)}

/* process */
.process{height:477px;background:var(--brand)}
.process .section-title{top:53px}
.process svg{position:absolute;left:0;top:0}
.step-label{position:absolute;font-family:"Roboto",sans-serif;font-weight:700;font-size:18px;color:var(--white);text-align:center;width:150px}
.step-text{position:absolute;width:220px;text-align:center;color:var(--white);font-size:12px;line-height:19px}

/* testimonials */
.testimonials{height:344px;background:var(--white)}
.testimonials .section-title{top:52px}
.quote{position:absolute;top:116px;width:320px}
.quote .avatar{position:absolute;left:0;top:0;width:79px;height:79px;border-radius:50%;background:linear-gradient(160deg,#d8dde3,#8b95a0);border:3px solid #eee}
.quote .text{position:absolute;left:96px;top:0;width:220px;font-size:12.5px;line-height:19.5px;color:#333}
.quote .text::before{content:"\201C\201C";color:#999;font-weight:700;margin-right:4px}
.quote .who{position:absolute;left:96px;top:168px;font-size:12px;line-height:19px}
.quote .who b{display:block;color:var(--brand);font-weight:600}
.quote .who span{font-weight:700;color:var(--ink)}
.q1{left:61px}.q2{left:439px}.q3{left:818px}

/* footer */
.footer{height:160px;background:var(--footer)}
.fcol{position:absolute;top:34px}
.fcol h4{font-family:"Roboto",sans-serif;font-weight:500;font-size:17px;color:var(--white);padding-bottom:10px;border-bottom:1px solid #555;width:265px;position:relative}
.fcol h4::after{content:"";position:absolute;left:0;bottom:-1px;width:40px;height:2px;background:var(--brand)}
.fcol p{margin-top:16px;font-size:15px;line-height:26px;color:var(--footer-text)}
.f1{left:61px}.f2{left:403px}.f2 h4{width:165px}.f3{left:644px}.f3 h4{width:250px}.f4{left:966px}.f4 h4{width:173px}
.socials{display:flex;gap:7px;margin-top:16px}
.socials b{width:24px;height:24px;border-radius:50%;background:#2a8fcf;border:1px solid #6cb8e6}
.socials b:nth-child(4){background:#e8a21c;border-color:#f3c36b}
.socials b:nth-child(5){background:#d9d9d9;border-color:#fff}
.copyright{height:50px;background:var(--footer-deep);color:#aaa;font-size:12px;text-align:center;line-height:50px}
</style>
</head>
<body>

<header class="topbar">
  <div class="contact">
    <span><i class="ico"><svg width="12" height="12" viewBox="0 0 24 24"><path fill="#fff" d="M6.6 10.8a15.1 15.1 0 0 0 6.6 6.6l2.2-2.2c.3-.3.7-.4 1-.2 1.1.4 2.3.6 3.6.6.6 0 1 .4 1 1V20c0 .6-.4 1-1 1A17 17 0 0 1 3 4c0-.6.4-1 1-1h3.5c.6 0 1 .4 1 1 0 1.3.2 2.5.6 3.6.1.3 0 .7-.2 1z"/></svg></i>+1 (555) 014 2290</span>
    <span><i class="ico"><svg width="12" height="10" viewBox="0 0 24 18"><path fill="#fff" d="M0 0h24v18H0zM2 2v1l10 7 10-7V2z"/></svg></i>info@beaconadvisoryinc.example</span>
  </div>
  <div class="follow"><em>Follow Us:</em><i><b></b></i><i><b></b></i><i><b></b></i></div>
</header>

<header class="nav">
  <div class="brand"><span class="mark"></span><span class="name">Beacon Advisory</span></div>
  <ul class="menu">
    <li class="active">COMPANY</li><li>SERVICES</li><li>SOLUTIONS</li><li>RESOURCES</li><li>CAREER</li><li>CONTACT US</li>
  </ul>
</header>

<section class="hero">
  <div class="photo" role="img" aria-label="Dimmed photo of business people reviewing charts at a desk"></div>
  <h1>ATTRACTING AND DEVELOPING</h1>
  <div class="line1">THE BEST TALENT FOR OUR BUSINESS,</div>
  <div class="line2">STRETCHING OUR PEOPLE AND DEVELOPING A <strong>“CAN DO”</strong> ATTITUDE.</div>
  <span class="btn">Read More</span>
</section>

<section class="welcome">
  <svg class="bg" width="1200" height="313"><polygon points="595,0 1200,0 1200,313 650,313" fill="#f1f1f1"/></svg>
  <h2><i></i>Welcome to Beacon Advisory</h2>
  <div class="copy">
    <p>Through the commitment of our employees and innovative engineering, we provide highly-reliable flexible circuits, heaters, sensors, instruments, integrated products and services that maximize our customers' competitive advantage.</p>
    <p>Delivering real value to our clients by providing top quality technical services and solutions at reasonable rates.</p>
    <p>Delivering real value to shareholders through consistent growth and strong profitability. Delivering the best work environment for our consultants and staff.</p>
  </div>
  <span class="btn">Read More</span>
  <div class="devices" role="img" aria-label="Laptop, tablet and phone showing app icons"></div>
</section>

<section class="services">
  <h2 class="section-title">OUR SERVICES</h2>
  <div class="card c1"><div class="pic" role="img" aria-label="Hand touching a digital technology interface"></div><div class="body"><h3>Technology</h3><p>consectetuer adipiscing elit, sed diam nonummy nibh euismod</p><span class="more">READ MORE »</span></div></div>
  <div class="card c2"><div class="pic" role="img" aria-label="Business handshake"></div><div class="body"><h3>Business</h3><p>consectetuer adipiscing elit, sed diam nonummy nibh euismod</p><span class="more">READ MORE »</span></div></div>
  <div class="card c3"><div class="pic" role="img" aria-label="Connected gears with app icons"></div><div class="body"><h3>Application Development</h3><p>consectetuer adipiscing elit, sed diam nonummy nibh euismod</p><span class="more">READ MORE »</span></div></div>
  <div class="card c4"><div class="pic" role="img" aria-label="Person working on a laptop"></div><div class="body"><h3>Enterprise Integration</h3><p>consectetuer adipiscing elit, sed diam nonummy nibh euismod</p><span class="more">READ MORE »</span></div></div>
  <div class="card c5"><div class="pic" role="img" aria-label="Hand holding a smartphone over a keyboard"></div><div class="body"><h3>IT Consulting</h3><p>consectetuer adipiscing elit, sed diam nonummy nibh euismod</p><span class="more">READ MORE »</span></div></div>
</section>

<section class="process">
  <h2 class="section-title">OUR PROCESSS</h2>
  <svg width="1200" height="477">
    <g stroke="#1577b8" stroke-width="5" stroke-dasharray="3 7" fill="none" stroke-linecap="round">
      <line x1="420" y1="230" x2="520" y2="275"/>
      <line x1="690" y1="255" x2="785" y2="215"/>
    </g>
    <circle cx="335" cy="203" r="82" fill="#fff"/>
    <polygon points="380,250 432,295 400,225" fill="#fff"/>
    <circle cx="335" cy="203" r="70" fill="#1b55a6"/>
    <circle cx="599" cy="279" r="82" fill="#fff"/>
    <polygon points="650,240 700,220 660,285" fill="#fff"/>
    <circle cx="599" cy="279" r="70" fill="#5ca72b"/>
    <circle cx="875" cy="203" r="82" fill="#fff"/>
    <circle cx="875" cy="203" r="70" fill="#333"/>
  </svg>
  <div class="step-label" style="left:260px;top:192px">EXAMINE</div>
  <div class="step-label" style="left:524px;top:268px">UNDERSTAND</div>
  <div class="step-label" style="left:800px;top:192px">DELIVER</div>
  <div class="step-text" style="left:225px;top:300px">consectetuer adipiscing elit, sed diam nonummy nibh euismod adipiscing elit.</div>
  <div class="step-text" style="left:489px;top:378px">consectetuer adipiscing elit, sed diam nonummy nibh euismod adipiscing elit.</div>
  <div class="step-text" style="left:765px;top:300px">consectetuer adipiscing elit, sed diam nonummy nibh euismod adipiscing elit.</div>
</section>

<section class="testimonials">
  <h2 class="section-title">TESTIMONIALS</h2>
  <div class="quote q1"><div class="avatar" role="img" aria-label="Portrait of client"></div><p class="text">Consectetuer adipiscing elit, s diam nonummy nibh euismodunt ut laoreet dolore magna aliquam era volutpat. Ut wisi enim ad miim venim, quis nostrud exerci tation ullamper suscipit lobortis nisl ut aliquip ex commodo consequat. ullamper suscipit lobortis.</p><div class="who"><b>MARK DALTON CEO</b><span>Lorem Ipsum dolar site</span></div></div>
  <div class="quote q2"><div class="avatar" role="img" aria-label="Portrait of client"></div><p class="text">Consectetuer adipiscing elit, s diam nonummy nibh euismodunt ut laoreet dolore magna aliquam era volutpat. Ut wisi enim ad miim venim, quis nostrud exerci tation ullamper suscipit lobortis nisl ut aliquip ex commodo consequat. ullamper suscipit lobortis.</p><div class="who"><b>MARK DALTON CEO</b><span>Lorem Ipsum dolar site</span></div></div>
  <div class="quote q3"><div class="avatar" role="img" aria-label="Portrait of client"></div><p class="text">Consectetuer adipiscing elit, s diam nonummy nibh euismodunt ut laoreet dolore magna aliquam era volutpat. Ut wisi enim ad miim venim, quis nostrud exerci tation ullamper suscipit lobortis nisl ut aliquip ex commodo consequat. ullamper suscipit lobortis.</p><div class="who"><b>MARK DALTON CEO</b><span>Lorem Ipsum dolar site</span></div></div>
</section>

<footer class="footer">
  <div class="fcol f1"><h4>ADDRESS</h4><p>Level 7, Consectetuer Street&nbsp; Diam<br>nonummy, NSW 0000</p></div>
  <div class="fcol f2"><h4>PHONE</h4><p>+1 (555) 014 2290</p></div>
  <div class="fcol f3"><h4>EMAIL</h4><p>info@beaconadvisoryinc.example</p></div>
  <div class="fcol f4"><h4>FOLLOW US</h4><div class="socials"><b></b><b></b><b></b><b></b><b></b></div></div>
</footer>
<footer class="copyright">Copyright @ Beacon Advisory</footer>

</body>
</html>
```